Design a modern, premium front panel for a stand-up pouch

Design a modern, premium front for a stand-up pouch for VELUTRA. Product is for Urine/vomit/runny stool incidents indoors; quick cleanups before smell sets; nighttime/elderly pet accidents; travel/car mishaps.

It must instantly show it’s for dogs & cats and include three small step icons with labels: Sprinkle → Wait 1–5 min → Sweep. Front copy to include: VELUTRA, descriptor “Mineral Instant Absorber – for Dogs & Cats”, one benefits line “Fragrance-Free • 100 % Mineral • Odor-Binding • Low-Dust

Goal: clear who/what/how in under 3 seconds
Deliverables: AI/PDF + a pouch mockup;

Target Market(s)

• Dog & cat households in apartments/homes; new pet parents, senior pets, multi-pet homes. • Cleanliness & odor-sensitive buyers (allergies/asthma, fragrance-free preference). • Surfaces at risk: carpets/rugs, sofas, mattresses, car interiors.

Industry/Entity Type

Pet e-commerce and retail

Font styles to use
Other font styles liked:
• like attached images

Requirements
Nice to have
• light background, eco friendly

```html
<!DOCTYPE html>
<html lang="en">
<head>
<meta charset="utf-8">
<title>VELUTRA – Mineral Instant Absorber pouch front</title>
<link rel="stylesheet" href="https://fonts.googleapis.com/css2?family=Poppins:wght@300;400;500&display=swap">
<style>
  :root {
    --canvas-bg: #e9e9e9;
    --panel-light: #efefee;
    --pattern-tone: #e4e3dc;
    --olive: #a8a286;
    --charcoal: #2f2f2f;
    --charcoal-deep: #252525;
    --ink: #2b2b2b;
    --pill: #3a3a3a;
    --pill-text: #f2f2f2;
    --white: #ffffff;
    --muted: #c9c9c4;
  }
  * { margin: 0; padding: 0; box-sizing: border-box; }
  html, body {
    width: 1200px; height: 800px; overflow: hidden;
    background: var(--canvas-bg);
    font-family: "Poppins", sans-serif;
  }
  .stage {
    width: 1200px; height: 800px;
    display: flex; align-items: center; justify-content: center;
  }
  .pouch-front {
    position: relative;
    width: 450px; height: 760px;
    background: var(--panel-light);
    overflow: hidden;
    border-radius: 6px;
  }
  .top-band {
    position: absolute; left: 0; top: 0; right: 0; height: 150px;
    background: linear-gradient(180deg, var(--charcoal) 0%, var(--charcoal-deep) 100%);
  }
  .top-band .seal-line {
    position: absolute; left: 0; right: 0; top: 48px; height: 2px;
    background: #1c1c1c;
  }
  .pattern-field {
    position: absolute; left: 82px; top: 150px; right: 0; bottom: 104px;
    background: linear-gradient(160deg, var(--panel-light) 0%, var(--pattern-tone) 100%);
  }
  .brand-strip {
    position: absolute; left: 0; top: 150px; width: 82px; bottom: 104px;
    background: var(--olive);
  }
  .brand-mark {
    position: absolute; left: 9px; top: 14px;
    width: 64px; height: 64px; border-radius: 50%;
    background: linear-gradient(150deg, #e6e4da, #c9c5b2);
    border: 2px solid var(--white);
  }
  .brand-name {
    position: absolute; left: 41px; top: 340px;
    transform: translate(-50%, -50%) rotate(-90deg);
    white-space: nowrap;
    font-weight: 300; font-size: 54px; letter-spacing: 8px;
    color: var(--white);
  }
  .product-title {
    position: absolute; left: 112px; top: 192px;
    font-weight: 400; font-size: 42px; line-height: 42px;
    color: var(--ink); letter-spacing: -0.3px;
  }
  .product-for {
    position: absolute; left: 118px; top: 334px;
    font-weight: 400; font-size: 17px; color: var(--ink);
  }
  .steps {
    position: absolute; left: 210px; top: 500px;
    list-style: none;
  }
  .step {
    position: relative; display: flex; align-items: center;
    width: 190px; height: 26px; margin-bottom: 24px;
    background: var(--pill); border-radius: 13px;
    color: var(--pill-text);
  }
  .step-num {
    font-size: 8px; font-weight: 400; margin-left: 12px; width: 46px;
    letter-spacing: 0.3px;
  }
  .step-label { font-size: 10px; font-weight: 400; letter-spacing: 0.3px; }
  .step-icon {
    position: absolute; right: -8px; top: 50%; transform: translateY(-50%);
    width: 40px; height: 40px; border-radius: 50%;
    background: var(--white); border: 1.5px solid var(--pill);
    display: flex; align-items: center; justify-content: center;
  }
  .bottom-band {
    position: absolute; left: 0; right: 0; bottom: 0; height: 104px;
    background: linear-gradient(180deg, var(--charcoal) 0%, var(--charcoal-deep) 100%);
  }
  .benefits {
    position: absolute; left: 0; right: 0; top: 16px;
    text-align: center; font-size: 11px; font-weight: 300;
    color: var(--muted); letter-spacing: 0.2px;
  }
</style>
</head>
<body>
<main class="stage">
  <section class="pouch-front">
    <div class="top-band"><div class="seal-line"></div></div>

    <div class="pattern-field" role="img" aria-label="Soft repeating pattern of paw prints and bones"></div>

    <div class="brand-strip">
      <div class="brand-mark" role="img" aria-label="Round badge with a dog and cat illustration"></div>
      <div class="brand-name">VELUTRA</div>
    </div>

    <h1 class="product-title">Mineral<br>Instant<br>Absorber</h1>
    <p class="product-for">— for Dogs &amp; Cats —</p>

    <ol class="steps">
      <li class="step">
        <span class="step-num">STEP 1</span><span class="step-label">SPRINKLE</span>
        <span class="step-icon">
          <svg width="24" height="24" viewBox="0 0 24 24" fill="#3a3a3a">
            <circle cx="12" cy="5" r="1.6"/><circle cx="7" cy="9" r="1.6"/><circle cx="17" cy="9" r="1.6"/>
            <circle cx="12" cy="12" r="1.8"/><circle cx="6" cy="15" r="1.4"/><circle cx="18" cy="15" r="1.4"/>
            <circle cx="10" cy="18" r="1.6"/><circle cx="14" cy="18" r="1.6"/><circle cx="12" cy="8.5" r="1"/>
          </svg>
        </span>
      </li>
      <li class="step">
        <span class="step-num">STEP 2</span><span class="step-label">WAIT 1–5 MIN</span>
        <span class="step-icon">
          <svg width="26" height="26" viewBox="0 0 26 26" fill="none" stroke="#3a3a3a" stroke-width="1.4">
            <circle cx="13" cy="13" r="10"/>
            <path d="M13 6v7l4 4" stroke-linecap="round"/>
          </svg>
        </span>
      </li>
      <li class="step">
        <span class="step-num">STEP 3</span><span class="step-label">SWEEP</span>
        <span class="step-icon">
          <svg width="26" height="26" viewBox="0 0 26 26" fill="none" stroke="#3a3a3a" stroke-width="1.6" stroke-linecap="round">
            <path d="M18 4l-5 10"/>
            <path d="M9 13l7 3-2 6-8-3z" fill="#3a3a3a"/>
          </svg>
        </span>
      </li>
    </ol>

    <div class="bottom-band">
      <p class="benefits">Fragrance Free • 100% Mineral • Odor Binding • Low Dust</p>
    </div>
  </section>
</main>
</body>
</html>
```